依頼詳細
今回は、トップページデザインの募集になります。
レスポンシブデザインのサイトで、bootstrap4を利用しコーディングする予定になります。
デザイン幅は2000px、コンテンツの幅はbootstrap4デフォルトの1110pxを基準としてください。ただし最近のデザインの流行を取りいれて、フルワイドや、1200~15000px程度の幅のコンテンツをバランスよくレイアウトしてください。
コンテンツ配置は基本12分割になります。がデザインによっては、多少逸脱してもかまいません。
念のため、サンプルのPSDデータを添付しますので、参照ください。

本文のフォントはゴシック系は游ゴシック、メイリオ、明朝系は遊明朝でお願いします。
飾り文字はフリーフォントか、googleフォントを利用してください。

メイン画像部分・グローバルメニューは、ワイド適用でお願いします。

資料上はサイト名(社名)や住所などは伏字にしております。ご提案時点ではそのまま作成をお願いします。当選確定後、本内容に修正をお願いいたします。

当選の方は、希望があれば引き続き下層ページの作成及びコーディング作業を依頼可能です。
不明点、質問などありましたらメッセージ等でご連絡ください。

・カラー
青系(爽やかなイメージ)

・掲載画像
必ず添付ファイルを使用してください。
また、雰囲気が合っていれば、指定外の画像を背景などに使用いただいてもOKです。

・その他
内容詳細に関しては、別添のExcel資料を参照してください。
サイトURL
ページ数
1ページ
希望イメージ
シンプル 複雑
単色 カラフル
暗い 明るい
日常 高級
遊び心 厳粛
未来的 伝統的
女性的 男性的
希望する色
青系、水色系
納品ファイル
• 高解像度JPG (.jpg)
• フォトショップ形式 (.psd)
補足説明
納品ファイルは、PDF及びクライアント表示確認用のJPGを準備お願いします。
■ 選んだ理由

今回は、贅沢さや豪華さをイメージさせる洗練された先進的なデザインを希望しており、見た目が大事な案件でした。
業界的に国内外問わず「サイトの見た目」をかなり重要視しているため、"見栄えのするデザイン"というところに重きを置いてクライアントとの折衝の結果、velbornさかた様を選定させていただきました。

■ 提案者全員のお礼・コメント

どの案も制作意図を組んでいただきとてもよかったのですが、今回はvelbornさかた様を当選とさせていただきました。
皆様ご提案ありがとうございました。
今後ともご提案宜しくお願いいたします。

```html
<!DOCTYPE html>
<html lang="ja">
<head>
<meta charset="utf-8">
<title>〇〇株式会社 | Safety High Quality</title>
<link rel="stylesheet" href="https://fonts.googleapis.com/css2?family=Cormorant+Garamond:wght@500;600&family=Great+Vibes&family=Noto+Sans+JP:wght@400;500;700&family=Noto+Serif+JP:wght@500;600&display=swap">
<style>
:root{
  --navy:#1c2a6b;
  --navy-deep:#141f55;
  --blue:#2b3f9a;
  --ink:#333;
  --muted:#777;
  --line:#d9dce6;
  --pale:#eef1fa;
  --lavender:#d6dcf2;
  --gold:#a79977;
  --white:#fff;
}
*{margin:0;padding:0;box-sizing:border-box}
html,body{width:1200px;height:2180px;overflow:hidden;background:var(--white)}
body{font-family:"Noto Sans JP",sans-serif;color:var(--ink);position:relative}
.serif{font-family:"Noto Serif JP",serif}
.en{font-family:"Cormorant Garamond",serif}

/* header */
.site-header{position:absolute;top:0;left:0;width:1200px;height:60px;z-index:3;display:flex;align-items:center;padding:0 140px 0 260px;justify-content:space-between}
.logo{width:160px;height:30px;background:rgba(255,255,255,.85);display:flex;align-items:center;justify-content:center;font-size:12px;color:var(--navy);font-weight:500}
.global-nav{display:flex;gap:26px;margin-top:12px}
.global-nav a{color:var(--white);text-decoration:none;text-align:center;font-family:"Cormorant Garamond",serif;font-size:13px;line-height:1.1;letter-spacing:.05em}
.global-nav small{display:block;font-family:"Noto Sans JP",sans-serif;font-size:7px;opacity:.85}
.lang{position:absolute;top:6px;right:140px;display:flex;gap:6px}
.lang span{width:14px;height:8px;background:rgba(255,255,255,.8)}

/* hero */
.hero{position:absolute;top:0;left:0;width:1200px;height:480px;background:linear-gradient(180deg,#7fb6e6 0%,#a9cdea 25%,#d9e3ea 38%,#5b93b8 55%,#2d6f96 75%,#3f7f6a 100%)}
.hero-title{position:absolute;top:170px;left:0;width:1200px;text-align:center;color:var(--white);font-family:"Cormorant Garamond",serif;font-weight:600;font-size:62px;line-height:1;text-shadow:0 2px 8px rgba(20,31,85,.35)}
.hero-script{position:absolute;top:312px;left:0;width:1200px;text-align:center;font-family:"Great Vibes",cursive;font-size:30px;color:rgba(255,255,255,.6)}

/* intro */
.intro{position:absolute;top:530px;left:0;width:1200px;text-align:center}
.intro h2{font-size:18px;font-weight:500;color:var(--navy);letter-spacing:.08em}
.intro p{font-size:11px;color:var(--muted);margin-top:20px;line-height:2.4}

/* cards */
.cards-band{position:absolute;top:760px;left:0;width:1200px;height:220px;background:var(--pale)}
.card{position:absolute;top:700px;width:320px;height:262px;background:var(--white);box-shadow:0 4px 14px rgba(28,42,107,.08)}
.card.company{left:268px}
.card.safety{left:628px;width:304px}
.card-photo{height:100px}
.company .card-photo{background:linear-gradient(135deg,#e7e9ee,#c8ccd6)}
.safety .card-photo{background:linear-gradient(135deg,#f3f4f6,#cfd4dc 60%,#9aa3b2)}
.card-body{height:162px;background:linear-gradient(180deg,var(--lavender),#eef1fa);text-align:center;padding-top:10px;position:relative}
.card-icon{width:44px;height:44px;border-radius:50%;background:#aeb9e4;margin:-32px auto 6px;display:flex;align-items:center;justify-content:center}
.card-body h3{font-family:"Cormorant Garamond",serif;font-size:16px;color:var(--navy);letter-spacing:.12em;font-weight:600}
.card-body small{display:block;font-size:8px;color:var(--muted)}
.card-body p{font-size:9px;color:var(--muted);margin-top:14px}

/* bus */
.bus{position:absolute;top:1020px;left:0;width:1200px;height:200px;background:linear-gradient(90deg,#b7c4d2 0%,#dbe3ec 30%,#8fa7c3 55%,#c9d2dc 80%,#9aa9b8 100%)}
.bus-box{position:absolute;top:40px;left:420px;width:400px;height:140px;background:var(--white);text-align:center;padding-top:26px;box-shadow:0 4px 14px rgba(0,0,0,.12)}
.bus-box h3{font-family:"Cormorant Garamond",serif;font-size:18px;color:var(--navy);letter-spacing:.15em}
.bus-box small{display:block;font-size:8px;color:var(--muted)}
.btn-more{display:inline-block;margin-top:18px;width:250px;height:24px;line-height:24px;background:var(--gold);color:var(--white);font-size:9px;border-radius:12px}

/* information */
.information{position:absolute;top:1340px;left:268px;width:672px;display:flex}
.info-head{width:170px}
.info-head h3{font-family:"Cormorant Garamond",serif;font-size:17px;color:var(--navy);letter-spacing:.08em}
.info-head small{font-size:8px;color:var(--muted)}
.info-list{flex:1;border-top:1px solid var(--line)}
.info-list li{list-style:none;display:flex;gap:20px;padding:12px 10px;border-bottom:1px solid var(--line);font-size:9px;line-height:1.8}
.info-list time{color:var(--muted);width:60px}
.tag{display:inline-block;background:var(--navy);color:var(--white);font-size:7px;padding:0 6px;margin-left:6px}

/* contact */
.contact{position:absolute;top:1620px;left:0;width:1200px;height:340px;background:linear-gradient(180deg,#c9d0ee 0%,#b2bde4 50%,#8d9ccf 100%)}
.contact-box{position:absolute;top:60px;left:372px;width:456px;height:232px;background:var(--white);text-align:center;padding-top:28px;box-shadow:0 4px 18px rgba(28,42,107,.15)}
.contact-box h3{font-family:"Cormorant Garamond",serif;font-size:18px;color:var(--navy);letter-spacing:.15em}
.contact-box small{display:block;font-size:8px;color:var(--muted)}
.tel-row{display:flex;justify-content:center;gap:36px;margin-top:20px;font-size:20px;color:var(--navy);font-family:"Cormorant Garamond",serif;font-weight:600}
.tel-row span{display:flex;align-items:center;gap:4px}
.btn-mail{display:inline-flex;align-items:center;gap:8px;justify-content:center;margin-top:16px;width:230px;height:28px;background:var(--navy);color:var(--white);font-size:10px;border-radius:14px}
.contact-note{font-size:8px;color:var(--muted);margin-top:12px}

/* footer */
.site-footer{position:absolute;top:1995px;left:0;width:1200px;height:150px}
.footer-brand{position:absolute;left:268px;top:12px;display:flex;align-items:center;gap:8px;font-size:12px;font-weight:500;color:var(--navy)}
.footer-brand i{width:22px;height:14px;background:#ccd2e6;display:block}
.footer-address{position:absolute;left:268px;top:40px;font-size:8px;color:var(--muted);line-height:1.8}
.footer-links{position:absolute;left:660px;top:14px;font-size:8px;color:var(--muted);display:flex;gap:10px}
.to-top{position:absolute;left:892px;top:52px;width:40px;height:40px;background:var(--gold);display:flex;align-items:center;justify-content:center}
.copyright{position:absolute;bottom:0;left:0;width:1200px;height:32px;background:var(--navy-deep);color:rgba(255,255,255,.7);font-size:8px;text-align:center;line-height:32px}
</style>
</head>
<body>

<section class="hero" role="img" aria-label="海沿いの高層ビル群とヤシの木、港に停泊するボートの写真"></section>
<header class="site-header">
  <div class="logo">Logo</div>
  <nav class="global-nav">
    <a href="#">HOME<small>ホーム</small></a>
    <a href="#">COMPANY<small>会社概要</small></a>
    <a href="#">BUS<small>バス紹介</small></a>
    <a href="#">SAFETY<small>安全への取り組み</small></a>
    <a href="#">CONTACT<small>お問い合わせ</small></a>
  </nav>
  <div class="lang"><span></span><span></span><span></span></div>
</header>
<h1 class="hero-title">Safety<br>High Quality</h1>
<p class="hero-script">with Comfort Travel</p>

<section class="intro">
  <h2 class="serif">より一層安全・安心なお客様サービスの実現へ</h2>
  <p>〇〇〇〇は「Safety」「High Quality」をモットーに、<br>これからも「最高の安全・安心」と「最高級の乗り心地」の提供を目指してまいります。</p>
</section>

<div class="cards-band"></div>
<article class="card company">
  <div class="card-photo" role="img" aria-label="オフィスビルの外観写真"></div>
  <div class="card-body">
    <div class="card-icon"><svg width="20" height="20" viewBox="0 0 20 20"><rect x="4" y="3" width="12" height="15" fill="none" stroke="#fff" stroke-width="1.5"/><path d="M7 7h2M11 7h2M7 11h2M11 11h2" stroke="#fff" stroke-width="1.5"/></svg></div>
    <h3>COMPANY</h3><small>会社概要</small>
    <p>会社の成り立ちと理念、事業内容をご紹介します。</p>
  </div>
</article>
<article class="card safety">
  <div class="card-photo" role="img" aria-label="打ち合わせをするスーツ姿の社員の写真"></div>
  <div class="card-body">
    <div class="card-icon"><svg width="20" height="20" viewBox="0 0 20 20"><path d="M10 2l6 3v5c0 4-3 6.5-6 8-3-1.5-6-4-6-8V5z" fill="none" stroke="#fff" stroke-width="1.5"/><path d="M7 10l2 2 4-4" fill="none" stroke="#fff" stroke-width="1.5"/></svg></div>
    <h3>SAFETY</h3><small>安全への取り組み</small>
    <p>安全・安心のための日々の取り組みをご紹介します。</p>
  </div>
</article>

<section class="bus" role="img" aria-label="車庫に並ぶ白い大型観光バスと建物の写真">
  <div class="bus-box">
    <h3>BUS</h3><small>バス紹介</small>
    <span class="btn-more">詳細はこちら ›</span>
  </div>
</section>

<section class="information">
  <div class="info-head"><h3>INFORMATION</h3><small>お知らせ</small></div>
  <ul class="info-list">
    <li><time>2021.00.00</time><span>テキストテキストテキスト<br>テキストテキスト<span class="tag">NEW</span></span></li>
    <li><time>2021.00.00</time><span>テキストテキストテキスト<br>テキストテキスト</span></li>
    <li><time>2021.00.00</time><span>テキストテキストテキスト<br>テキストテキスト</span></li>
  </ul>
</section>

<section class="contact" role="img" aria-label="青みがかった街並みとバスの写真">
  <div class="contact-box">
    <h3>CONTACT</h3><small>お問い合わせ</small>
    <div class="tel-row">
      <span><svg width="14" height="14" viewBox="0 0 14 14"><path d="M3 1l2 3-1.5 1.5a8 8 0 0 0 5 5L10 9l3 2-1 2c-6 0-11-5-11-11z" fill="#1c2a6b"/></svg>000-0000-0000</span>
      <span><svg width="14" height="14" viewBox="0 0 14 14"><rect x="2" y="4" width="10" height="7" fill="none" stroke="#1c2a6b" stroke-width="1.3"/><rect x="4" y="1" width="6" height="3" fill="#1c2a6b"/></svg>000-0000-0000</span>
    </div>
    <span class="btn-mail"><svg width="12" height="9" viewBox="0 0 12 9"><rect x=".5" y=".5" width="11" height="8" fill="none" stroke="#fff"/><path d="M.5.5l5.5 4 5.5-4" fill="none" stroke="#fff"/></svg>メールフォーム ›</span>
    <p class="contact-note">受付時間 平日 9:00〜18:00（土日祝を除く）</p>
  </div>
</section>

<footer class="site-footer">
  <div class="footer-brand"><i></i>〇〇株式会社</div>
  <p class="footer-address">〒000-0000 〇〇県〇〇市〇〇町0-0-0<br>TEL 000-0000-0000<br>FAX 000-0000-0000</p>
  <nav class="footer-links"><span>ホーム</span><span>会社概要</span><span>バス紹介</span><span>安全への取り組み</span><span>お問い合わせ</span></nav>
  <div class="to-top"><svg width="12" height="8" viewBox="0 0 12 8"><path d="M1 7l5-5 5 5" fill="none" stroke="#fff" stroke-width="1.5"/></svg></div>
</footer>
<div class="copyright">© 〇〇株式会社 All Rights Reserved.</div>

</body>
</html>
```